Word Document Estimate Sheet

Good evening. I have an home renovations company that does a lot of estimates through word documents and then emailed them a PDF document. MarqueFold did my logo and stationary projects and did a great job with it. Now I need my word document estimate sheet to be more standardized meaning sometimes my headers and footers move when I get to the bottom of the page , this make me have to do a copy and paste many times to put them back in their place also I have headings like Master Bedroom, Master Bath . I would like for them to always be bold, underlined and colon on the end now I always have to do this. I would like for the header and footers to not move when I get to the bottom of the page. Basically I want the same document with the same look as the document I send but with less retyping and copy and pasting. Hopefully this makes sense and you can help my estimates go faster.

Thanks,
Lem

Target Market(s)

Customer who want an estimate

Industry/Entity Type

It Company

Requirements
Must have
• 1.Must have same header and footer as the document I sent but want text to be standard.
• 2.Header and footer must not move when I get to the bottom of page.
• 3.Categories like Master Bedroom, Kitchen Area categories must already be in the document and if I want to delete them I can.
Nice to have
• I would love my estimate time to be cut in half because new word estimate sheet is simple to work with.
Should not have
• Don't change the header and footer design at all just make sure it doesn't move when I type.

```html
<!DOCTYPE html>
<html lang="en">
<head>
<meta charset="utf-8">
<title>Estimate Sheet – Calder Home Renovations</title>
<link rel="stylesheet" href="https://fonts.googleapis.com/css2?family=Tinos:wght@400;700&display=swap">
<style>
  :root {
    --desk-top: #ffffff;
    --desk-bottom: #eeeeee;
    --desk-rule: #d6d6d6;
    --page: #ffffff;
    --page-edge: #c9c9c9;
    --header-fill: #f2f2f4;
    --brand-band: #8a83a7;
    --brand-name: #8a83a7;
    --ink: #000000;
  }
  * { margin: 0; padding: 0; box-sizing: border-box; }
  html, body { width: 1200px; height: 610px; overflow: hidden; }
  body {
    position: relative;
    background: linear-gradient(to bottom, var(--desk-top), var(--desk-bottom));
    border-top: 1px solid var(--desk-rule);
    font-family: "Tinos", "Times New Roman", serif;
    color: var(--ink);
  }
  .sheet {
    position: absolute;
    left: 155px; top: 20px;
    width: 868px; height: 620px;
    background: var(--page);
    border: 1px solid var(--page-edge);
  }
  .letterhead {
    position: absolute;
    left: 2px; right: 2px; top: 0;
    height: 109px;
    background: var(--header-fill);
    display: flex; align-items: flex-end; justify-content: center;
    padding-bottom: 14px;
  }
  .brand-name {
    font-family: "Tinos", "Times New Roman", serif;
    font-weight: 700;
    font-size: 30px;
    letter-spacing: 1px;
    color: var(--brand-name);
  }
  .letterhead-band {
    position: absolute;
    left: 2px; right: 2px; top: 109px;
    height: 16px;
    background: var(--brand-band);
  }
  .room-heading,
  .task {
    position: absolute;
    font-size: 16.5px;
    line-height: 22px;
  }
  .room-heading {
    left: 104px;
    font-weight: 700;
    text-decoration: underline;
    text-underline-offset: 2px;
  }
  .task { left: 157px; width: 600px; }
  .task::before {
    content: "";
    position: absolute;
    left: -46px; top: 8px;
    width: 6px; height: 6px;
    border-radius: 50%;
    background: var(--ink);
  }
</style>
</head>
<body>
  <main class="sheet">
    <header class="letterhead">
      <span class="brand-name">Calder Home Renovations</span>
    </header>
    <div class="letterhead-band"></div>

    <h2 class="room-heading" style="top:140px">Master Bathroom:</h2>
    <p class="task" style="top:182px">Repair ceiling and wall in stated area then prime and paint entire bathroom.</p>
    <p class="task" style="top:236px">Clean &amp; paint all base molding in stated area a semi-gloss white color</p>
    <p class="task" style="top:291px">Clean and paint door case molding on all 3 sides a semi-gloss white.</p>
    <p class="task" style="top:332px">Clean door in stated area first and if it’s determined it needs to be painted we will<br>discuss with customer for pricing before painting it.</p>

    <h2 class="room-heading" style="top:413px">Bedroom #2:</h2>
    <p class="task" style="top:455px">Clean &amp; paint all base molding in stated area a semi-gloss white color</p>
    <p class="task" style="top:509px">Clean and paint door case molding on all 3 sides a semi-gloss white.</p>
    <p class="task" style="top:550px">Clean doors in stated area first and if it’s determined it needs to be painted we will<br>discuss with customer for pricing before painting it</p>
  </main>
</body>
</html>
```